Property risk and finance brokerage company needs a business card design

Tarlow Financial requires a business card design. Please integrate existing logo (refer uploaded file).
hex codes used on logo #002649 #008ED6 #444F51 #ADAFAA
font used - Cinzel
Contact information
Renata Sollisford
Director
Mobile: 0491 738 205
email: r.sollisford@tarlowfinancial.example.au
website: www.tarlowfinancial.example.au
CRN : 918354
PO Box 527
Canterbury, Victoria, 3126
Horizontal orientation please
Finance

```html
<!DOCTYPE html>
<html lang="en">
<head>
<meta charset="utf-8">
<title>Tarlow Financial – Business Card</title>
<link rel="stylesheet" href="https://fonts.googleapis.com/css2?family=Cinzel:wght@400&family=Open+Sans:wght@400;700&display=swap">
<style>
  :root {
    --backdrop: #e9e6e1;
    --card-black: #1c1b1b;
    --navy: #002649;
    --brand-blue: #008ED6;
    --band-deep: #1d4ea3;
    --band-light: #5cb8ec;
    --slate: #444F51;
    --silver: #ADAFAA;
    --white: #ffffff;
  }
  * { box-sizing: border-box; margin: 0; padding: 0; }
  html, body {
    width: 1200px;
    height: 666px;
    overflow: hidden;
    background: var(--backdrop);
  }
  .sheet {
    position: relative;
    width: 1200px;
    height: 666px;
    display: flex;
    justify-content: center;
    align-items: center;
    gap: 60px;
  }
  .card {
    position: relative;
    width: 520px;
    height: 298px;
    background: var(--card-black);
    box-shadow: 0 6px 18px rgba(0,0,0,0.28);
    overflow: hidden;
  }
  .card__band {
    position: absolute;
    left: 0;
    right: 0;
    bottom: 0;
    height: 24px;
    background: linear-gradient(90deg, var(--band-deep) 0%, var(--brand-blue) 40%, var(--band-light) 62%, var(--brand-blue) 80%, var(--band-deep) 100%);
  }
  .card__band::before {
    content: "";
    position: absolute;
    left: 0; right: 0; top: 0;
    height: 2px;
    background: rgba(255,255,255,0.25);
  }

  /* Front */
  .brand {
    position: absolute;
    left: 0;
    right: 0;
    top: 92px;
    display: flex;
    justify-content: center;
    align-items: center;
    gap: 20px;
  }
  .brand__mark {
    width: 70px;
    height: 70px;
    border-radius: 50%;
    background: var(--brand-blue);
  }
  .brand__name {
    font-family: "Cinzel", serif;
    font-weight: 400;
    font-size: 42px;
    line-height: 1.05;
    color: var(--brand-blue);
    letter-spacing: 1px;
  }

  /* Back */
  .contact {
    position: absolute;
    left: 32px;
    top: 44px;
    font-family: "Open Sans", sans-serif;
    color: var(--white);
  }
  .contact__name {
    font-size: 19px;
    font-weight: 700;
    line-height: 1.1;
  }
  .contact__role {
    font-size: 11px;
    margin-left: 6px;
    margin-top: 2px;
  }
  .contact__address {
    font-size: 13px;
    line-height: 1.4;
    margin-top: 26px;
    margin-left: 16px;
  }
  .contact__lines {
    list-style: none;
    font-size: 13px;
    line-height: 1.45;
    margin-top: 18px;
    margin-left: 32px;
    white-space: nowrap;
  }
  .contact__label { font-weight: 700; }
  .contact__divider { font-weight: 700; padding: 0 4px; }
  .back__mark {
    position: absolute;
    right: 44px;
    top: 44px;
    width: 104px;
    height: 104px;
    border-radius: 50%;
    background: var(--brand-blue);
  }
</style>
</head>
<body>
<main class="sheet">
  <section class="card card--front" aria-label="Business card front">
    <div class="brand">
      <span class="brand__mark" aria-hidden="true"></span>
      <p class="brand__name">Tarlow<br>Financial</p>
    </div>
    <div class="card__band"></div>
  </section>

  <section class="card card--back" aria-label="Business card back">
    <div class="contact">
      <p class="contact__name">Renata Sollisford</p>
      <p class="contact__role">Director</p>
      <p class="contact__address">PO Box 527,<br>Canterbury, Victoria, 3126.</p>
      <ul class="contact__lines">
        <li><span class="contact__label">Cell :</span> 0491 738 205<span class="contact__divider">|</span><span class="contact__label">CRN</span> 918354</li>
        <li><span class="contact__label">E-mail :</span> r.sollisford@tarlowfinancial.example.au</li>
        <li><span class="contact__label">Web :</span> www.tarlowfinancial.example.au</li>
      </ul>
    </div>
    <span class="back__mark" aria-hidden="true"></span>
    <div class="card__band"></div>
  </section>
</main>
</body>
</html>
```